New Packaging Design Project

Wine packaging redesign. Retail partner requested a redesign of a private label wine. The old label is attached. Our partner liked the Lantern and Briar label and wanted something similar. There will be a logo added to the top of the label

Went on vacation/holiday

```html
<!DOCTYPE html>
<html lang="en">
<head>
<meta charset="utf-8">
<title>Corva Ridge Red Blend Label</title>
<link rel="stylesheet" href="https://fonts.googleapis.com/css2?family=Oswald:wght@400;500&display=swap">
<style>
  :root {
    --backdrop: #e8e8e8;
    --label-black: #1c1c1c;
    --emblem-fill: #262626;
    --foil-gold: #b8955e;
  }
  html, body {
    margin: 0;
    padding: 0;
    width: 1200px;
    height: 801px;
    overflow: hidden;
    background: var(--backdrop);
  }
  .canvas {
    position: relative;
    width: 1200px;
    height: 801px;
    display: flex;
    align-items: center;
    justify-content: center;
  }
  .label {
    position: relative;
    width: 440px;
    height: 640px;
    background: var(--label-black);
    box-sizing: border-box;
    padding: 24px;
  }
  .label__frame {
    width: 100%;
    height: 100%;
    border: 1px solid var(--foil-gold);
    box-sizing: border-box;
    display: flex;
    flex-direction: column;
    align-items: center;
    color: var(--foil-gold);
    font-family: "Oswald", sans-serif;
    text-transform: uppercase;
    text-align: center;
  }
  .brand {
    margin-top: 78px;
    display: flex;
    flex-direction: column;
    align-items: center;
    gap: 6px;
  }
  .brand__name {
    font-size: 22px;
    font-weight: 400;
    letter-spacing: 0.32em;
    margin-right: -0.32em;
  }
  .brand__vintage {
    font-size: 17px;
    font-weight: 400;
    letter-spacing: 0.32em;
    margin-right: -0.32em;
  }
  .emblem {
    margin-top: 26px;
    display: block;
  }
  .wine-type {
    margin-top: 46px;
    font-size: 24px;
    font-weight: 500;
    letter-spacing: 0.12em;
    margin-right: -0.12em;
  }
  .varietals {
    margin-top: 26px;
    font-size: 11px;
    font-weight: 400;
    letter-spacing: 0.1em;
    line-height: 1.7;
  }
</style>
</head>
<body>
  <main class="canvas">
    <section class="label">
      <div class="label__frame">
        <header class="brand">
          <span class="brand__name">Corva Ridge</span>
          <span class="brand__vintage">2018</span>
        </header>
        <svg class="emblem" width="200" height="200" viewBox="0 0 200 200" role="img" aria-label="Winery emblem: mountain peaks over rolling vineyard rows">
          <circle cx="100" cy="100" r="100" fill="var(--emblem-fill)"/>
        </svg>
        <h1 class="wine-type">Red Blend</h1>
        <p class="varietals">
          Merlot | Cabernet Sauvignon<br>
          Cabernet Franc | Petit Verdot | Malbec
        </p>
      </div>
    </section>
  </main>
</body>
</html>
```